create a Wedding Invitation design

Personalized wedding invitation using names, initials, a nice monogram with decorative border

incorporate names: Lena and Osmond (first names)
Halvorsk (surname)
and wedding date , April 12, 2014

Colors: black ink on white;
optional accent colors: bright pink, bright orange, cajun red (may be flowers)
No shades of Purple

Industry/Entity Type

Wedding

Requirements
Must have
• Romantic, slightly formal looking design, black on white ; some accent color preferred, monogram (using first names Lena and Osmond and last name Halvorsk), that could be isolated and used on RSVP cards preferred
Nice to have
• idea of being at the top of a building (venue is called Brightmoor Hall) - the wedding is being held on the 17th floor of building with panoramic views of Washington DC and the mountains ; Washington DC skyline, iconic DC cherry blossoms

Here are some examples of a typical Washington, DC skyline (this is an optional or secondary feature only - not to dominate the design):
http://www.pictovane.com/clip-art/washington-dc.html#comp.asp?recid=48113760&xtra=
Cherry blossoms : http://www.jaunterly.com/news/story_8146.html

```html
<!DOCTYPE html>
<html lang="en">
<head>
<meta charset="utf-8">
<title>Lena &amp; Osmond Halvorsk — Wedding Invitation</title>
<link rel="stylesheet" href="https://fonts.googleapis.com/css2?family=Alegreya:ital,wght@1,400&family=Alike&display=swap">
<style>
  :root {
    --paper: #ffffff;
    --ink: #111111;
    --blossom-light: #fbd3e0;
    --blossom: #f6a3bf;
    --blossom-deep: #f07a9f;
    --branch: #8a7360;
    --leaf: #a9dcc8;
    --monogram-orange: #f28a12;
  }
  * { margin: 0; padding: 0; box-sizing: border-box; }
  html, body { width: 1200px; height: 849px; overflow: hidden; background: var(--paper); }
  .invitation {
    position: relative;
    width: 1200px;
    height: 849px;
    background: var(--paper);
    color: var(--ink);
    font-family: "Alike", Georgia, serif;
  }
  .blossom-branch {
    position: absolute;
    left: 15px;
    top: 0;
    width: 335px;
    height: 849px;
  }
  .text-block { position: absolute; line-height: 1; white-space: nowrap; }
  .script {
    font-family: "Alegreya", "Palatino Linotype", serif;
    font-style: italic;
    font-weight: 400;
  }
  .name { left: 410px; font-size: 64px; }
  .name--bride { top: 146px; }
  .name--groom { top: 290px; }
  .connector { left: 412px; top: 240px; font-size: 24px; }
  .invite-line { left: 412px; top: 406px; font-size: 26px; }
  .occasion { left: 410px; top: 460px; font-size: 42px; }
  .details {
    left: 412px;
    top: 565px;
    font-size: 25px;
    line-height: 34px;
  }
  .venue { left: 412px; top: 671px; font-size: 25px; }
  .rsvp {
    left: 740px;
    top: 765px;
    font-size: 25px;
    line-height: 33px;
  }
  .monogram {
    position: absolute;
    left: 983px;
    top: 60px;
    width: 162px;
    height: 186px;
    display: flex;
    flex-direction: column;
    align-items: center;
    justify-content: center;
    gap: 12px;
    color: var(--monogram-orange);
    font-family: "Alike", Georgia, serif;
    font-size: 15px;
    line-height: 1.2;
    text-align: center;
  }
  .monogram-dot {
    width: 22px;
    height: 22px;
    border-radius: 50%;
    background: var(--monogram-orange);
  }
</style>
</head>
<body>
  <main class="invitation">
    <svg class="blossom-branch" viewBox="0 0 335 849" role="img" aria-label="Illustration of a cherry blossom branch with pink flowers and mint leaves">
      <defs>
        <linearGradient id="blossomTone" x1="0" y1="0" x2="0" y2="1">
          <stop offset="0" stop-color="var(--blossom)"/>
          <stop offset="0.5" stop-color="var(--blossom-light)"/>
          <stop offset="1" stop-color="var(--blossom)"/>
        </linearGradient>
      </defs>
      <rect x="0" y="0" width="335" height="849" fill="url(#blossomTone)"/>
    </svg>

    <p class="text-block script name name--bride">Lena Halvorsk</p>
    <p class="text-block connector">and</p>
    <p class="text-block script name name--groom">Osmond Halvorsk</p>
    <p class="text-block invite-line">invite you to share in their</p>
    <p class="text-block script occasion">Wedding Celebration</p>
    <p class="text-block details">Saturday, 12 th April 2014<br>at 7.00 p.m.</p>
    <p class="text-block venue">Venue: Any Hotel (Address)</p>
    <p class="text-block rsvp">RSVP date<br>phone&nbsp; / email</p>

    <div class="monogram">
      <span class="monogram-dot"></span>
      <span class="monogram-names">Lena Halvorsk<br>Osmond Halvorsk</span>
    </div>
  </main>
</body>
</html>
```